A4 Flyer

Bright Path Learning is starting a course in regional Victoria. We are currently advertising (See attached file A34984) in local papers but need to create a one page flyer to distribute to Aged Care facilities in the area. The A4 flyer will be inserted into a folder pack with more detailed information on Bright Path Learning. Important to use images and logoes attached

Target Market(s)

Flyer to be distributed to Aged Care facility staff and owners

Industry/Entity Type

Advertising

Font styles to use
Sans Serif

Colors
f37123
ec1f27

Requirements
Must have
• BPL Logo
Some image

```html
<!DOCTYPE html>
<html lang="en">
<head>
<meta charset="utf-8">
<title>Bright Path Learning – Fast Track Course Flyer</title>
<link href="https://fonts.googleapis.com/css2?family=Arimo:ital,wght@0,400;0,700;1,400&display=swap" rel="stylesheet">
<style>
  :root {
    --orange: #f37123;
    --red-orange: #ec4f27;
    --deep-orange: #e8562a;
    --amber: #f58a2f;
    --yellow: #fcc814;
    --gold: #f8b50f;
    --ink: #4a4a4a;
    --ink-soft: #5c5c5c;
    --cream: #fdf3ea;
    --page-bg: #e9e6e2;
    --white: #ffffff;
  }
  * { box-sizing: border-box; margin: 0; padding: 0; }
  html, body { width: 1200px; height: 1000px; overflow: hidden; }
  body {
    background: var(--page-bg);
    font-family: "Arimo", Arial, sans-serif;
    color: var(--ink);
    position: relative;
  }
  .flyer {
    position: absolute;
    left: 266px; top: 67px;
    width: 667px; height: 865px;
    background: linear-gradient(180deg, var(--white) 0, var(--white) 170px, var(--cream) 260px, var(--white) 560px, var(--white) 100%);
    box-shadow: 0 6px 24px rgba(0,0,0,.18);
    overflow: hidden;
  }
  .flyer-art { position: absolute; left: 0; top: 0; width: 667px; height: 865px; }
  .abs { position: absolute; }

  .brand { left: 38px; top: 40px; display: flex; align-items: center; gap: 12px; }
  .brand-dot { width: 38px; height: 38px; border-radius: 50%; background: var(--orange); }
  .brand-name { font-size: 27px; line-height: 29px; font-weight: 400; color: var(--orange); letter-spacing: .5px; }

  .badge-text { text-align: center; font-style: italic; line-height: 1.1; }
  .badge-start { left: 386px; top: 64px; width: 100px; font-size: 15px; color: var(--white); transform: rotate(-8deg); }
  .badge-unique { left: 488px; top: 52px; width: 130px; font-size: 18px; font-weight: 700; font-style: italic; color: var(--ink); transform: rotate(4deg); }

  .headline { left: 40px; top: 130px; width: 600px; text-align: center; font-size: 30px; font-weight: 700; color: var(--white); transform: rotate(-2.2deg); text-shadow: 0 1px 2px rgba(0,0,0,.15); }

  .course-title { left: 35px; top: 219px; font-size: 21px; font-weight: 700; color: var(--red-orange); }
  .course-venue { left: 35px; top: 248px; font-size: 14px; font-style: italic; color: var(--ink-soft); }
  .qual-label { left: 35px; top: 279px; font-size: 15px; color: var(--ink-soft); }
  .qual-name { left: 35px; top: 300px; font-size: 17px; line-height: 22px; font-weight: 700; color: var(--ink); }

  .funding { left: 35px; top: 367px; font-size: 20px; line-height: 26px; font-weight: 700; color: var(--red-orange); }

  .funding-note { left: 35px; top: 471px; font-size: 12px; line-height: 16px; color: var(--ink-soft); width: 240px; }

  .topic-list { left: 35px; top: 510px; list-style: none; }
  .topic-list li { font-size: 13px; font-weight: 700; color: var(--ink); height: 22.4px; display: flex; align-items: center; gap: 8px; }
  .tick { width: 11px; height: 11px; flex: none; }

  .mission { left: 35px; top: 696px; width: 440px; font-size: 12px; line-height: 17px; color: var(--ink-soft); }

  .contact-label { font-size: 16px; font-weight: 700; color: var(--ink-soft); }
  .contact-value { font-size: 20px; font-weight: 700; color: var(--ink); margin-top: 6px; }
  .contact-phone { left: 35px; top: 758px; }
  .contact-web { left: 210px; top: 758px; }
  .contact-divider { left: 186px; top: 756px; width: 1px; height: 50px; background: var(--orange); }

  .enroll { left: 548px; top: 786px; width: 90px; text-align: center; font-size: 22px; line-height: 24px; font-weight: 700; color: var(--ink); transform: rotate(-6deg); }
</style>
</head>
<body>
<main class="flyer">
  <svg class="flyer-art" viewBox="0 0 667 865" xmlns="http://www.w3.org/2000/svg">
    <defs>
      <polygon id="burst" points="50,0 40.6,10.9 43.3,25 29.7,29.7 25,43.3 10.9,40.6 0,50 -10.9,40.6 -25,43.3 -29.7,29.7 -43.3,25 -40.6,10.9 -50,0 -40.6,-10.9 -43.3,-25 -29.7,-29.7 -25,-43.3 -10.9,-40.6 0,-50 10.9,-40.6 25,-43.3 29.7,-29.7 43.3,-25 40.6,-10.9"/>
      <linearGradient id="band" x1="0" y1="0" x2="0" y2="1">
        <stop offset="0" stop-color="#f58a2f"/>
        <stop offset="1" stop-color="#e8562a"/>
      </linearGradient>
      <linearGradient id="photoA" x1="0" y1="0" x2="1" y2="1">
        <stop offset="0" stop-color="#eef0f2"/><stop offset="1" stop-color="#c9a58c"/>
      </linearGradient>
      <linearGradient id="photoB" x1="0" y1="0" x2="0" y2="1">
        <stop offset="0" stop-color="#f1f3f5"/><stop offset="1" stop-color="#a99c95"/>
      </linearGradient>
      <linearGradient id="photoC" x1="0" y1="0" x2="0" y2="1">
        <stop offset="0" stop-color="#f3efea"/><stop offset="1" stop-color="#6e5a50"/>
      </linearGradient>
      <marker id="arrowhead" viewBox="0 0 10 10" refX="5" refY="5" markerWidth="7" markerHeight="7" orient="auto-start-reverse">
        <path d="M0,0 L10,5 L0,10 z" fill="#f37123"/>
      </marker>
      <marker id="arrowheadGold" viewBox="0 0 10 10" refX="5" refY="5" markerWidth="7" markerHeight="7" orient="auto-start-reverse">
        <path d="M0,0 L10,5 L0,10 z" fill="#fcc814"/>
      </marker>
    </defs>

    <!-- headline band -->
    <path d="M0,125 Q330,100 667,112 L667,170 Q330,175 0,190 Z" fill="url(#band)"/>
    <path d="M0,178 Q330,165 667,160 L667,170 Q330,175 0,190 Z" fill="#d94a22" opacity=".5"/>

    <!-- badges -->
    <use href="#burst" transform="translate(436 92) rotate(-8) scale(0.9)" fill="#ec5a28"/>
    <use href="#burst" transform="translate(553 72) rotate(5) scale(1.2 0.95)" fill="#fcc814"/>

    <!-- dotted dividers -->
    <line x1="30" y1="355" x2="310" y2="355" stroke="#f37123" stroke-width="2" stroke-dasharray="2 3"/>
    <line x1="30" y1="456" x2="310" y2="456" stroke="#f37123" stroke-width="2" stroke-dasharray="2 3"/>

    <!-- image rings -->
    <circle cx="482" cy="383" r="120" fill="#ec5a28"/>
    <circle cx="482" cy="383" r="82" fill="url(#photoA)" role="img" aria-label="Photo of a trainer demonstrating on an anatomy model"/>
    <circle cx="339" cy="555" r="82" fill="#f58a2f"/>
    <circle cx="339" cy="555" r="58" fill="url(#photoB)" role="img" aria-label="Portrait photo of a male course trainer"/>
    <circle cx="517" cy="600" r="82" fill="#fcc814"/>
    <circle cx="517" cy="600" r="58" fill="url(#photoC)" role="img" aria-label="Portrait photo of a female course trainer"/>

    <!-- cycle arrows -->
    <path d="M377,273 Q322,300 330,375" fill="none" stroke="#f37123" stroke-width="1.5" marker-end="url(#arrowhead)"/>
    <path d="M340,672 Q270,680 248,622" fill="none" stroke="#f37123" stroke-width="1.5" marker-end="url(#arrowhead)"/>
    <path d="M555,714 Q625,712 640,645" fill="none" stroke="#fcc814" stroke-width="1.5" marker-end="url(#arrowheadGold)"/>

    <!-- footer band -->
    <path d="M0,835 Q330,820 667,812 L667,865 L0,865 Z" fill="url(#band)"/>
    <path d="M0,830 Q330,815 667,806 L667,812 Q330,820 0,835 Z" fill="#fcc814"/>

    <!-- enrol badge -->
    <use href="#burst" transform="translate(593 810) rotate(-6) scale(1.3 1.2)" fill="#fcc814"/>
  </svg>

  <div class="abs brand">
    <span class="brand-dot"></span>
    <span class="brand-name">bright path<br>learning</span>
  </div>

  <p class="abs badge-text badge-start">Starts<br>July 2014</p>
  <p class="abs badge-text badge-unique">Unique<br>Opportunity</p>

  <h1 class="abs headline">Making You The Future Of Healthcare</h1>

  <h2 class="abs course-title">Fast Track Course</h2>
  <p class="abs course-venue">Greenvale Care Home – Stawell &nbsp;&nbsp;|&nbsp; 9:00am - 3:00pm</p>
  <p class="abs qual-label">Double Qualification</p>
  <p class="abs qual-name">CERT III IN AGED CARE WITH<br>HOME AND COMMUNITY CARE</p>

  <p class="abs funding">Government Funding<br>for eligible students!<br>Fees from $117</p>

  <p class="abs funding-note">This training is delivered with VIC and Comm Govt Funding to eligible students</p>

  <ul class="abs topic-list">
    <li><svg class="tick" viewBox="0 0 12 12"><path d="M1,6 L4.5,10 L11,1" fill="none" stroke="#ec4f27" stroke-width="1.8"/></svg>Pathology</li>
    <li><svg class="tick" viewBox="0 0 12 12"><path d="M1,6 L4.5,10 L11,1" fill="none" stroke="#ec4f27" stroke-width="1.8"/></svg>Aged Care</li>
    <li><svg class="tick" viewBox="0 0 12 12"><path d="M1,6 L4.5,10 L11,1" fill="none" stroke="#ec4f27" stroke-width="1.8"/></svg>First Aid</li>
    <li><svg class="tick" viewBox="0 0 12 12"><path d="M1,6 L4.5,10 L11,1" fill="none" stroke="#ec4f27" stroke-width="1.8"/></svg>CPR</li>
    <li><svg class="tick" viewBox="0 0 12 12"><path d="M1,6 L4.5,10 L11,1" fill="none" stroke="#ec4f27" stroke-width="1.8"/></svg>Anaphylaxis</li>
    <li><svg class="tick" viewBox="0 0 12 12"><path d="M1,6 L4.5,10 L11,1" fill="none" stroke="#ec4f27" stroke-width="1.8"/></svg>Home &amp; Community Care</li>
    <li><svg class="tick" viewBox="0 0 12 12"><path d="M1,6 L4.5,10 L11,1" fill="none" stroke="#ec4f27" stroke-width="1.8"/></svg>Medications for PCA’s</li>
    <li><svg class="tick" viewBox="0 0 12 12"><path d="M1,6 L4.5,10 L11,1" fill="none" stroke="#ec4f27" stroke-width="1.8"/></svg>Health Services</li>
  </ul>

  <p class="abs mission">Bright Path Learning aims to provide professional, accredited and accessible training courses in order to increase your knowledge and strengthen your skills.</p>

  <div class="abs contact-phone">
    <p class="contact-label">Call us on</p>
    <p class="contact-value">03 9000 4120</p>
  </div>
  <div class="abs contact-divider"></div>
  <div class="abs contact-web">
    <p class="contact-label">To enrol visit us at</p>
    <p class="contact-value">www.brightpathlearning.com.au</p>
  </div>

  <p class="abs enroll">Enroll<br>Now!!</p>
</main>
</body>
</html>
```